Gymnastics Award Design Needed--for kids

Need a gymnastics certificate or award designed. Will be printed on a piece of 8.5x11 paper. The award will be celebrating the gymnast learning a new skill in gymnastics. So it should be fun, but still look "official". Needs to look good hanging on a gymnast's bedroom wall.

It should say "The Aerial Cartwheel Club"
I will be using this design to change it based on the skill.

My main colors are:
#34475D
#E1467A
#7555A4

So should use those, but can add others

My website is tumblenest.net so you can see the look/feel.

Target Market(s)

Main audience will be girls ages 5-12, but will also be used by slightly older girls and boys. So needs to be fun, not too gender specific.

Industry/Entity Type

Learning

Requirements
Must have
• The following will need to go on the certificate:
• * Name of Skill
• * Image of Skill
• * Gymnast's Name
• * my logo
• * Gym's Logo
• * Gym's Name
• Optional: Date

```html
<!DOCTYPE html>
<html lang="en">
<head>
<meta charset="utf-8">
<title>Aerial Cartwheel Club Certificate</title>
<link rel="stylesheet" href="https://fonts.googleapis.com/css2?family=Amatic+SC:wght@700&family=League+Gothic&family=Raleway:wght@300;400&family=Great+Vibes&display=swap">
<style>
  :root {
    --pink: #E1467A;
    --purple: #5E3A98;
    --violet: #7555A4;
    --paper: #FFFFFF;
    --skin: #E9B48E;
    --suit-red: #E03A3E;
    --suit-blue: #36A9DF;
    --suit-yellow: #F6B23A;
  }
  html, body {
    margin: 0;
    padding: 0;
    width: 1200px;
    height: 848px;
    overflow: hidden;
    background: var(--pink);
  }
  .certificate {
    position: relative;
    width: 1200px;
    height: 848px;
    font-family: "Raleway", sans-serif;
  }
  .frame {
    position: absolute;
    inset: 0;
  }
  .title {
    position: absolute;
    top: 30px;
    left: 0;
    width: 100%;
    margin: 0;
    text-align: center;
    font-family: "Amatic SC", cursive;
    font-weight: 700;
    font-size: 172px;
    line-height: 1;
    color: var(--pink);
    letter-spacing: 2px;
  }
  .subtitle {
    position: absolute;
    top: 198px;
    left: 0;
    width: 100%;
    margin: 0;
    text-align: center;
    font-family: "League Gothic", sans-serif;
    font-weight: 400;
    font-size: 86px;
    line-height: 1;
    color: var(--purple);
  }
  .ribbon {
    position: absolute;
    top: 198px;
    width: 54px;
    height: 96px;
  }
  .ribbon--left { left: 345px; }
  .ribbon--right { left: 799px; }
  .presented {
    position: absolute;
    top: 278px;
    left: 0;
    width: 100%;
    text-align: center;
    font-weight: 300;
    font-size: 29px;
    color: var(--purple);
    letter-spacing: -0.5px;
  }
  .recipient {
    position: absolute;
    top: 402px;
    left: 424px;
    width: 352px;
    text-align: center;
    font-family: "Amatic SC", cursive;
    font-weight: 700;
    font-size: 56px;
    line-height: 60px;
    color: var(--pink);
    border-bottom: 2px solid var(--pink);
  }
  .signature {
    position: absolute;
    top: 486px;
    left: 0;
    width: 100%;
    text-align: center;
    font-family: "Great Vibes", cursive;
    font-size: 64px;
    color: var(--purple);
  }
  .skill-figure {
    position: absolute;
    border-radius: 50% 50% 12px 12px;
  }
  .skill-figure--balance { left: 90px; top: 592px; width: 110px; height: 150px; background: linear-gradient(180deg, var(--skin), var(--suit-red)); }
  .skill-figure--walkover { left: 262px; top: 594px; width: 108px; height: 146px; background: linear-gradient(180deg, var(--skin), var(--suit-yellow)); }
  .skill-figure--leap { left: 718px; top: 614px; width: 222px; height: 104px; background: linear-gradient(90deg, var(--skin), var(--suit-blue), var(--skin)); border-radius: 50%; }
  .skill-figure--jump { left: 982px; top: 594px; width: 126px; height: 140px; background: linear-gradient(200deg, var(--skin), var(--suit-red)); }
  .beam {
    position: absolute;
    left: 90px;
    top: 736px;
    width: 102px;
    height: 8px;
    border-radius: 4px;
    background: #6B6B6B;
  }
  .floor-line {
    position: absolute;
    left: 260px;
    top: 737px;
    width: 112px;
    height: 1px;
    background: #D6D6D6;
  }
  .brand {
    position: absolute;
    top: 736px;
    left: 0;
    width: 100%;
    display: flex;
    justify-content: center;
    align-items: center;
    gap: 14px;
  }
  .brand__mark {
    width: 38px;
    height: 38px;
    border-radius: 50%;
    background: var(--violet);
  }
  .brand__name {
    font-family: "Raleway", sans-serif;
    font-weight: 400;
    font-size: 44px;
    letter-spacing: 1px;
    color: var(--pink);
  }
</style>
</head>
<body>
<main class="certificate">
  <svg class="frame" width="1200" height="848" viewBox="0 0 1200 848" aria-hidden="true">
    <rect width="1200" height="848" fill="var(--pink)"/>
    <path fill="var(--paper)" d="M138 22 H1062 A110 110 0 0 0 1164 94 V754 A110 110 0 0 0 1062 826 H138 A110 110 0 0 0 36 754 V94 A110 110 0 0 0 138 22 Z"/>
  </svg>

  <h1 class="title">Aerial Cartwheel</h1>

  <svg class="ribbon ribbon--left" viewBox="0 0 54 96" aria-hidden="true">
    <path fill="var(--purple)" d="M27 4 C14 4 10 16 14 28 L0 84 L0 96 L27 46 L54 96 L54 84 L40 28 C44 16 40 4 27 4 Z M27 12 C34 12 35 20 32 28 L27 38 L22 28 C19 20 20 12 27 12 Z"/>
  </svg>
  <h2 class="subtitle">Club Certificate</h2>
  <svg class="ribbon ribbon--right" viewBox="0 0 54 96" aria-hidden="true">
    <path fill="var(--purple)" d="M27 4 C14 4 10 16 14 28 L0 84 L0 96 L27 46 L54 96 L54 84 L40 28 C44 16 40 4 27 4 Z M27 12 C34 12 35 20 32 28 L27 38 L22 28 C19 20 20 12 27 12 Z"/>
  </svg>

  <p class="presented" style="margin:0">Presented to :</p>

  <div class="recipient">By Maya Tumble Nest</div>

  <div class="signature">signature</div>

  <div class="skill-figure skill-figure--balance" role="img" aria-label="Illustration of a gymnast in a red leotard balancing on a beam"></div>
  <div class="beam"></div>
  <div class="skill-figure skill-figure--walkover" role="img" aria-label="Illustration of a gymnast in yellow doing a walkover"></div>
  <div class="floor-line"></div>
  <div class="skill-figure skill-figure--leap" role="img" aria-label="Illustration of a gymnast in a blue leotard doing a split leap"></div>
  <div class="skill-figure skill-figure--jump" role="img" aria-label="Illustration of a gymnast in a red leotard doing a ring jump"></div>

  <div class="brand">
    <span class="brand__mark"></span>
    <span class="brand__name">TUMBLE NEST</span>
  </div>
</main>
</body>
</html>
```